Personal logo & business cards
for owner of multiple businesses.
Hi qlindo,
I really like your design #16. Can you maybe try it in a couple different colour combinations, and maybe also with the 'MIRELA VOSK' part in a cursive text?
Thanks,
Mirela
Hello porvadesign:
I like the design on 19 & 20, but I'd prefer it without the logo on the front. Also, there's maybe too much purple... it's a bit too feminine. Can you try it with less purple or in another colour?
Thanks!
I don't currently have a logo or anything... and would prefer that there wasn't a logo for one of my businesses on the front of my card. A personal logo would be okay though.
@PH - Any logo to use? Thanks
Hey everyone,
Please make sure to read the brief a little more closely. I only want my name and personal contact information on the front of the card, and the names of the THREE businesses that I am involved in on the back of the card.
Thanks for your submissions!
Open to colour palette, but leaning more towards purple or green. No blues.

```html
<!DOCTYPE html>
<html lang="en">
<head>
<meta charset="utf-8">
<title>Mirela Vosk – Business Cards</title>
<link href="https://fonts.googleapis.com/css2?family=Arimo:wght@400;700&display=swap" rel="stylesheet">
<style>
  :root {
    --stage: #2b2b2b;
    --card-white: #ffffff;
    --ink: #2a2a2a;
    --ink-soft: #555555;
    --swoosh-grey: #c9c9c9;
    --plum: #a8448f;
    --plum-light: #c65fae;
    --plum-accent: #6fae2d;
    --cobalt: #1e4fa6;
    --cobalt-light: #3a7ad6;
    --cobalt-dark: #0e2f6e;
    --crimson: #c41f27;
    --crimson-light: #e2403f;
    --crimson-dark: #8e1218;
  }
  * { box-sizing: border-box; margin: 0; padding: 0; }
  html, body { width: 1200px; height: 624px; overflow: hidden; }
  body {
    background: var(--stage);
    font-family: "Arimo", Arial, sans-serif;
    color: var(--ink);
  }
  .card-set {
    position: absolute;
    top: 139px;
    width: 288px;
  }
  .card-set--plum { left: 149px; --main: var(--plum); --main-light: var(--plum-light); --main-dark: #7e2c6a; --accent: var(--plum-accent); }
  .card-set--cobalt { left: 463px; --main: var(--cobalt); --main-light: var(--cobalt-light); --main-dark: var(--cobalt-dark); --accent: var(--cobalt); }
  .card-set--crimson { left: 756px; --main: var(--crimson); --main-light: var(--crimson-light); --main-dark: var(--crimson-dark); --accent: var(--crimson); }

  .card {
    position: relative;
    width: 288px;
    height: 149px;
    border-radius: 12px;
    overflow: hidden;
  }
  .card--front { background: var(--card-white); }
  .card--back {
    margin-top: 14px;
    background: radial-gradient(ellipse at 60% 40%, var(--main-light), var(--main) 55%, var(--main-dark));
    color: #ffffff;
    padding: 16px 20px;
  }
  .front-swoosh { position: absolute; inset: 0; width: 100%; height: 100%; }
  .front-swoosh .swoosh-shade { fill: var(--swoosh-grey); }
  .front-swoosh .swoosh-main { fill: var(--main); }
  .front-swoosh .swoosh-accent { fill: var(--accent); }

  .front-name {
    position: absolute; left: 18px; top: 22px;
    font-size: 19px; font-weight: 400; letter-spacing: -0.2px; color: var(--ink);
  }
  .front-fullname {
    position: absolute; left: 18px; top: 54px;
    font-size: 9.5px; color: var(--ink);
  }
  .front-contact {
    position: absolute; left: 18px; top: 76px;
    font-size: 5.5px; line-height: 7.4px; color: var(--ink-soft);
    list-style: none;
  }
  .front-contact .icon-line::before {
    content: ""; display: inline-block; width: 5px; height: 5px;
    background: var(--main); margin-right: 4px; vertical-align: -0.5px;
  }

  .business { margin-bottom: 9px; font-size: 9.5px; line-height: 11.5px; }
  .business-role { display: block; }
  .back-web {
    position: absolute; left: 0; right: 0; bottom: 5px;
    text-align: center; font-size: 5px; opacity: 0.85;
  }
</style>
</head>
<body>

<main class="card-sets">
  <section class="card-set card-set--plum">
    <article class="card card--front">
      <svg class="front-swoosh" viewBox="0 0 288 149" aria-hidden="true">
        <path class="swoosh-shade" d="M250 0 C240 78 190 126 96 149 L120 149 C205 128 252 78 262 0 Z"/>
        <path class="swoosh-accent" d="M262 0 C252 78 205 128 120 149 L150 149 C220 128 262 80 270 0 Z"/>
        <path class="swoosh-main" d="M270 0 C262 80 220 128 150 149 L288 149 L288 0 Z"/>
      </svg>
      <h2 class="front-name">MIRELA VOSK</h2>
      <p class="front-fullname">Mirela Vosk Trosdan</p>
      <ul class="front-contact">
        <li>48 Linden Crescent North</li>
        <li>Harwick, ON K7L 4P2</li>
        <li class="icon-line">555 014 2283</li>
        <li class="icon-line">555 014 2284</li>
        <li class="icon-line">mirela@vosktrosdan.com</li>
        <li class="icon-line">www.vosktrosdan.com</li>
      </ul>
    </article>
    <article class="card card--back">
      <p class="business">Mirela Vosk's Liquidation Supercentre<span class="business-role">President</span></p>
      <p class="business">Northgate Bargain Outlet<span class="business-role">President</span></p>
      <p class="business">Trosdan Group<span class="business-role">Partner</span></p>
      <p class="back-web">www.vosktrosdan.com</p>
    </article>
  </section>

  <section class="card-set card-set--cobalt">
    <article class="card card--front">
      <svg class="front-swoosh" viewBox="0 0 288 149" aria-hidden="true">
        <path class="swoosh-shade" d="M250 0 C240 78 190 126 96 149 L130 149 C212 126 254 78 262 0 Z"/>
        <path class="swoosh-main" d="M262 0 C254 78 212 126 130 149 L288 149 L288 0 Z"/>
      </svg>
      <h2 class="front-name">MIRELA VOSK</h2>
      <p class="front-fullname">Mirela Vosk Trosdan</p>
      <ul class="front-contact">
        <li>48 Linden Crescent North</li>
        <li>Harwick, ON K7L 4P2</li>
        <li class="icon-line">555 014 2283</li>
        <li class="icon-line">555 014 2284</li>
        <li class="icon-line">mirela@vosktrosdan.com</li>
        <li class="icon-line">www.vosktrosdan.com</li>
      </ul>
    </article>
    <article class="card card--back">
      <p class="business">Mirela Vosk's Liquidation Supercentre<span class="business-role">President</span></p>
      <p class="business">Northgate Bargain Outlet<span class="business-role">President</span></p>
      <p class="business">Trosdan Group<span class="business-role">Partner</span></p>
      <p class="back-web">www.vosktrosdan.com</p>
    </article>
  </section>

  <section class="card-set card-set--crimson">
    <article class="card card--front">
      <svg class="front-swoosh" viewBox="0 0 288 149" aria-hidden="true">
        <path class="swoosh-shade" d="M250 0 C240 78 190 126 96 149 L130 149 C212 126 254 78 262 0 Z"/>
        <path class="swoosh-main" d="M262 0 C254 78 212 126 130 149 L288 149 L288 0 Z"/>
      </svg>
      <h2 class="front-name">MIRELA VOSK</h2>
      <p class="front-fullname">Mirela Vosk Trosdan</p>
      <ul class="front-contact">
        <li>48 Linden Crescent North</li>
        <li>Harwick, ON K7L 4P2</li>
        <li class="icon-line">555 014 2283</li>
        <li class="icon-line">555 014 2284</li>
        <li class="icon-line">mirela@vosktrosdan.com</li>
        <li class="icon-line">www.vosktrosdan.com</li>
      </ul>
    </article>
    <article class="card card--back">
      <p class="business">Mirela Vosk's Liquidation Supercentre<span class="business-role">President</span></p>
      <p class="business">Northgate Bargain Outlet<span class="business-role">President</span></p>
      <p class="business">Trosdan Group<span class="business-role">Partner</span></p>
      <p class="back-web">www.vosktrosdan.com</p>
    </article>
  </section>
</main>

</body>
</html>
```